Seasoned logs and kindling for sale

producing firewood from beech,ash,oak and silver birch,
Kindling is produce from a variety of seasoned softwoods

Industry/Entity Type

Firewood

Contact Information for Business Card

peter Calloway 07831226904
alan Frickley 07854317620
e-mail,peterc817@mailbrook.example

```html
<!DOCTYPE html>
<html lang="en">
<head>
<meta charset="utf-8">
<title>Firewood Business Card</title>
<link rel="stylesheet" href="https://fonts.googleapis.com/css2?family=Lato:wght@400;700;900&display=swap">
<style>
  :root {
    --page-bg: #6b6b6b;
    --card-bg: #e2e5e8;
    --accent-red: #a3151b;
    --ink-black: #0d0d0d;
    --text-grey: #4a4a4a;
    --white: #ffffff;
    --wood-light: #d9a57a;
    --wood-dark: #8a5a3a;
  }
  * { margin: 0; padding: 0; box-sizing: border-box; }
  html, body {
    width: 1200px;
    height: 900px;
    overflow: hidden;
    background: var(--page-bg);
    font-family: "Lato", Arial, sans-serif;
  }
  .canvas {
    position: relative;
    width: 1200px;
    height: 900px;
  }
  .business-card {
    position: absolute;
    left: 100px;
    top: 165px;
    width: 1000px;
    height: 570px;
    background: var(--card-bg);
    overflow: hidden;
  }
  .email-badge {
    position: absolute;
    left: 606px;
    top: 50px;
    width: 372px;
    height: 58px;
    background: var(--accent-red);
    color: var(--white);
    display: flex;
    align-items: center;
    justify-content: center;
    gap: 12px;
    font-size: 21px;
    font-weight: 400;
    letter-spacing: 0.2px;
    white-space: nowrap;
  }
  .email-badge svg { width: 20px; height: 15px; flex: none; }
  .contact {
    position: absolute;
    left: 0;
  }
  .contact--first { top: 288px; }
  .contact--second { top: 424px; }
  .contact-tab {
    position: absolute;
    left: 0;
    top: 12px;
    width: 66px;
    height: 26px;
    background: var(--ink-black);
  }
  .contact-name {
    position: absolute;
    left: 80px;
    top: 0;
    white-space: nowrap;
    font-size: 41px;
    font-weight: 900;
    color: var(--accent-red);
    letter-spacing: -0.5px;
  }
  .contact-phone {
    position: absolute;
    left: 80px;
    top: 56px;
    display: flex;
    align-items: center;
    gap: 14px;
    white-space: nowrap;
    font-size: 30px;
    color: var(--text-grey);
    letter-spacing: 1px;
  }
  .contact-phone svg { width: 16px; height: 26px; flex: none; }
  .firewood-photo {
    position: absolute;
    left: 660px;
    top: 296px;
    width: 290px;
    height: 196px;
    border-radius: 40px 60px 30px 30px;
    background: radial-gradient(ellipse at 40% 45%, var(--wood-light) 0%, #c0875c 55%, var(--wood-dark) 100%);
  }
  .bottom-band {
    position: absolute;
    left: 0;
    bottom: 0;
    width: 1000px;
    height: 22px;
    background: var(--ink-black);
  }
</style>
</head>
<body>
<div class="canvas">
  <div class="business-card">
    <div class="email-badge">
      <svg viewBox="0 0 20 15" aria-hidden="true">
        <rect x="0" y="0" width="20" height="15" rx="1.5" fill="#ffffff"/>
        <path d="M1 1.5 L10 8.5 L19 1.5" fill="none" stroke="#a3151b" stroke-width="1.8"/>
      </svg>
      <span>peterc817@mailbrook.example</span>
    </div>

    <div class="contact contact--first">
      <div class="contact-tab"></div>
      <div class="contact-name">Alan Frickley</div>
      <div class="contact-phone">
        <svg viewBox="0 0 16 26" aria-hidden="true">
          <rect x="1" y="1" width="14" height="24" rx="2.5" fill="none" stroke="#4a4a4a" stroke-width="2"/>
          <rect x="3.5" y="4" width="9" height="14" fill="#4a4a4a"/>
          <circle cx="8" cy="21.5" r="1.4" fill="#4a4a4a"/>
        </svg>
        <span>078-543-17620</span>
      </div>
    </div>

    <div class="contact contact--second">
      <div class="contact-tab"></div>
      <div class="contact-name">Peter Calloway</div>
      <div class="contact-phone">
        <svg viewBox="0 0 16 26" aria-hidden="true">
          <rect x="1" y="1" width="14" height="24" rx="2.5" fill="none" stroke="#4a4a4a" stroke-width="2"/>
          <rect x="3.5" y="4" width="9" height="14" fill="#4a4a4a"/>
          <circle cx="8" cy="21.5" r="1.4" fill="#4a4a4a"/>
        </svg>
        <span>078-312-26904</span>
      </div>
    </div>

    <div class="firewood-photo" role="img" aria-label="Photograph of a stack of split seasoned firewood logs"></div>

    <div class="bottom-band"></div>
  </div>
</div>
</body>
</html>
```